Stationery Design Project

We need a stationery design to change our look to a more corporate design. My company has been established since 1989 and over that time has changed from your average sign company to doing more Corporate re branding projects and have some multi National clients.
Our website is currently being redesigned so we need a new logo and business cards etc. to compliment it.
I have 2 graphic designers employed but i want on outsiders opinion and a totally independant view point.
Updates
Hi Designers
We are predominantely a sign manufacturing company that manufacturers every type of sign you can imagine. However the majoprity of our work is digital graphics. Our claim to faim is that we wrap the Harbour Skytrams and Glidetrams which everyone seems to know in Sydney.We also do all sorts of Large format digital printing, vehicle wraps,vinyl signage,LED & Neon Illuminated signage,CNC Routing all materials,Laser cutting and Engraving, Architectural signage, Cut Out letters and Screenprinting.
Aswell as this we totally re-brand companies with internal wall graphics reception signage way finding signage and the like.We are a medium size company that has been trading since 1989 and has some very large reputable clients.
Our Company name is Brightmark Pty Ltd but like to have Signage and Graphics in our stationery.
Our details are as follows T: 9381 5027 F: 9381 5063 Unit 4, 22 Quarry Lane.Pine Flats. NSW 2163 email mail@brightmarkexample.com our current website is being re-designed www.brightmarkexample.com
The design and colour scheme i would like is quite simple with a corporate feel and blue, grey & magenta are colours that seem to suit but am open to most suggestions just looking for clean lines.
Hopefully this is enough information if you require any more please ask.
Regards Neil Barrowby
We are looking to simplify our LOGO not too concerned yet about layout of stationery items that we can easily work on later. I want to get a new logo that we can work with before we return to work on the 16th January so please concentrate on just the logo for now.
We would like to have Signs & Graphics somewhere in the name even though our registered name is Brightmark Pty Ltd. Brightmark is one word, i want it to be quite a bold font with no seriffs.The bright blue and grey colours are favourites so far with maybe a little magenta added later. Would like to have a Logo that is totally seperate and then the Brightmark P/L Signs & graphics as a secondary item just to let people know what Brightmark do as the name obviously does not say what we are about.
Also we need to consider how we can put logo on T-shirts work shirts and company vehicles.
We do not need CD cover or envelopes but letterheads and business cards.
Industry/Entity Type
Business
Look and feel
Each slider illustrates characteristics of the customer's brand and the style your logo design should communicate.

```html
<!DOCTYPE html>
<html lang="en">
<head>
<meta charset="utf-8">
<title>Brightmark Business Cards</title>
<link rel="stylesheet" href="https://fonts.googleapis.com/css2?family=Open+Sans:wght@400;600;800&display=swap">
<style>
  :root {
    --backdrop: #e9e6e1;
    --magenta: #ff2fbf;
    --sky: #7fe0ff;
    --blue: #00aeef;
    --ink: #111111;
    --muted: #8a8a8a;
    --paper: #ffffff;
    --accent-magenta: #9b2f7a;
    --accent-teal: #3a8c9a;
  }
  * { margin: 0; padding: 0; box-sizing: border-box; }
  html, body { width: 1200px; height: 900px; overflow: hidden; }
  body {
    position: relative;
    background: var(--backdrop);
    font-family: "Open Sans", sans-serif;
  }
  .card {
    position: absolute;
    border-radius: 22px;
    overflow: hidden;
    box-shadow: 0 4px 14px rgba(0,0,0,0.25);
  }
  .card-front {
    left: 24px; top: 20px; width: 821px; height: 462px;
    background: linear-gradient(to bottom, #ffffff 60%, #e8e8ea);
    z-index: 2;
  }
  .card-back {
    left: 370px; top: 430px; width: 804px; height: 450px;
    background: radial-gradient(ellipse at 20% 30%, #4a4a4a, #232323 75%);
    z-index: 1;
  }
  .front-header {
    position: absolute; left: 0; top: 0; width: 100%; height: 226px;
    background: linear-gradient(to bottom, #3f3f41 0%, #6e6e70 80%, var(--sky) 88%, var(--blue) 100%);
  }
  .back-accent {
    position: absolute;
    background: linear-gradient(to right, var(--accent-magenta), var(--accent-teal));
    opacity: 0.35;
    border-radius: 4px;
  }
  .back-accent.upper { left: 523px; top: 0; width: 187px; height: 173px; }
  .back-accent.lower { left: 430px; top: 277px; width: 192px; height: 173px; }
  .wordmark {
    position: absolute;
    display: flex; align-items: center; gap: 10px;
    color: var(--magenta);
    font-weight: 800;
    letter-spacing: 0.5px;
  }
  .wordmark .dot { border-radius: 50%; background: var(--magenta); }
  .card-front .wordmark { left: 26px; top: 24px; font-size: 44px; }
  .card-front .wordmark .dot { width: 34px; height: 34px; }
  .card-back .wordmark { left: 66px; top: 172px; font-size: 78px; }
  .card-back .wordmark .dot { width: 62px; height: 62px; }
  .holder { position: absolute; right: 24px; top: 240px; text-align: right; }
  .holder-name { font-size: 27px; color: var(--ink); line-height: 1.1; }
  .holder-role { font-size: 17px; color: var(--muted); font-weight: 600; }
  .address {
    position: absolute; left: 20px; top: 322px;
    font-size: 21px; line-height: 27px; color: var(--muted); font-style: normal;
  }
  .contact-line {
    position: absolute; left: 22px; top: 390px;
    display: flex; align-items: center; gap: 8px;
    font-size: 18px; color: var(--muted);
  }
  .contact-line .gap { width: 18px; }
  .email { position: absolute; left: 23px; top: 424px; font-size: 18px; color: var(--muted); }
  .web-front {
    position: absolute; right: 24px; top: 423px;
    font-size: 17px; color: var(--ink); font-weight: 600;
  }
  .web-back {
    position: absolute; left: 29px; top: 411px;
    font-size: 17px; color: #ffffff; font-weight: 600;
  }
</style>
</head>
<body>

<section class="card card-front">
  <div class="front-header" role="img" aria-label="Decorative grey header with blue accent bands"></div>

  <div class="wordmark"><span>BRIGHTMARK</span><span class="dot"></span></div>

  <div class="holder">
    <div class="holder-name">Martin Keswick</div>
    <div class="holder-role">Director</div>
  </div>

  <address class="address">Unit 5/18 Carver Street, Pine Flats<br>NSW 2163</address>

  <div class="contact-line">
    <svg width="28" height="28" viewBox="0 0 28 28" aria-label="Phone">
      <circle cx="14" cy="14" r="12.5" fill="none" stroke="#222" stroke-width="2"/>
      <path d="M9 7c1.5-1 2.5 0 3 1.5l0.6 1.6c0.3 0.9-0.3 1.5-1 2 0.8 1.8 2 3 3.6 3.8 0.5-0.7 1.1-1.3 2-1l1.6 0.6c1.5 0.5 2.4 1.5 1.4 3-1.2 1.6-3 1.8-5 0.8-3.3-1.6-5.9-4.4-7.1-7.6-0.7-2-0.5-3.6 0.9-4.7z" fill="#222"/>
    </svg>
    <span>(02) 9381 5027</span>
    <span class="gap"></span>
    <svg width="32" height="24" viewBox="0 0 32 24" aria-label="Fax">
      <path d="M8 3h14l2 8H8z" fill="#f4f4f4" stroke="#999"/>
      <rect x="2" y="11" width="28" height="9" rx="2" fill="#d6d6d6" stroke="#999"/>
      <rect x="6" y="20" width="20" height="2.5" fill="#aaa"/>
    </svg>
    <span>(02) 9381 5063</span>
  </div>

  <div class="email">Mail - mail@brightmarkexample.com</div>
  <div class="web-front">www.brightmarkexample.com</div>
</section>

<section class="card card-back">
  <div class="back-accent upper" role="img" aria-label="Decorative colour accent area"></div>
  <div class="back-accent lower" role="img" aria-label="Decorative colour accent area"></div>

  <div class="wordmark"><span>BRIGHTMARK</span><span class="dot"></span></div>

  <div class="web-back">www.brightmarkexample.com</div>
</section>

</body>
</html>
```